TR Ventura Website (professional site for investors and funds)

We want to make a website for an Holding Company that owns other companies' shares in different fields. TR is the name of the holding.
We still do not have a logo or preferred colors for the company. The company, through this website, will send a clear message: it's not important where we are, it's important what we do but more than that why we do what we do.
We search for inspiration in a simple layout because we want that the user feels comfortable and guided while exploring it. The content of the website aspire to be very impressive through one or more background images.

Below, the structure of the pages explained shortly.
To learn more, we have attached a draft of the website.

Home: page with a huge backround image that fill the whole page (maybe is better to merge the navbar with the image top color?).
About: with the same huge background image, we explain which are our fields.
Why: with the same huge background image, we explain which is our why.
Projects: dropdown list with project 1, project 2, project 3. If clicked, a box like about/why pops up in order to explain projects in detail.

Target Market(s)

Investors, Entrepreneurs

Industry/Entity Type

It Company

Number of Pages Required

4 page

Font styles to use
Sans Serif

Requirements
Must have
• An idea for the background image (color and design)
• Menu
• Page layout for about/why/projects
Nice to have
• Tips for color to use in this design
Should not have
• Complicated stuff

```html
<!DOCTYPE html>
<html lang="en">
<head>
<meta charset="UTF-8">
<title>TR Ventura</title>
<link href="https://fonts.googleapis.com/css2?family=Raleway:wght@400;500;600&family=Open+Sans:wght@400;600;700&display=swap" rel="stylesheet">
<style>
  :root {
    --navy: #0c1f4a;
    --deep-blue: #123a86;
    --blue: #1c63c4;
    --bright-blue: #2f8fe0;
    --sky: #8fb6dc;
    --sunset: #f0a247;
    --accent: #1a9be8;
    --nav-active: #2ab0f5;
    --white: #ffffff;
    --footer-bg: rgba(10, 22, 45, 0.82);
  }
  * { margin: 0; padding: 0; box-sizing: border-box; }
  html, body { width: 1200px; height: 743px; overflow: hidden; }
  body { font-family: "Open Sans", sans-serif; color: var(--white); }

  .page { position: relative; width: 1200px; height: 743px; overflow: hidden; }

  .hero-backdrop {
    position: absolute; inset: 0;
    background:
      radial-gradient(ellipse 420px 360px at 180px 640px, rgba(240,162,71,0.95), rgba(240,162,71,0) 70%),
      radial-gradient(ellipse 300px 420px at 140px 300px, rgba(200,215,235,0.75), rgba(200,215,235,0) 70%),
      radial-gradient(ellipse 520px 520px at 700px 520px, rgba(47,143,224,0.9), rgba(47,143,224,0) 75%),
      radial-gradient(ellipse 380px 420px at 1080px 460px, rgba(22,70,190,0.95), rgba(22,70,190,0) 75%),
      linear-gradient(180deg, var(--navy) 0%, var(--deep-blue) 30%, var(--blue) 60%, var(--deep-blue) 100%);
  }

  .site-header {
    position: absolute; top: 0; left: 0; right: 0; height: 126px;
    display: flex; align-items: center; justify-content: space-between;
    padding: 0 99px;
  }
  .brand {
    font-family: "Raleway", sans-serif; font-weight: 500;
    font-size: 25px; letter-spacing: 0.3px; color: var(--white);
  }
  .main-nav { display: flex; gap: 45px; }
  .main-nav a {
    font-family: "Raleway", sans-serif; font-weight: 600; font-size: 15px;
    color: var(--white); text-decoration: none; letter-spacing: 0.2px;
  }
  .main-nav a.is-active { color: var(--nav-active); }

  .hero {
    position: absolute; top: 190px; left: 0; right: 0; text-align: center;
  }
  .hero-title {
    font-family: "Raleway", sans-serif; font-weight: 500;
    font-size: 89px; line-height: 1; letter-spacing: 0.5px;
    text-shadow: 0 2px 8px rgba(0,0,0,0.3);
  }
  .hero-lead {
    margin: 32px auto 0; width: 720px;
    font-size: 26px; font-weight: 600; line-height: 38px;
    text-shadow: 0 1px 6px rgba(0,0,0,0.45);
  }
  .cta {
    display: inline-block; margin-top: 37px;
    width: 196px; height: 54px; line-height: 50px;
    border: 2px solid var(--white); border-radius: 27px;
    background: var(--accent); color: var(--white);
    font-weight: 700; font-size: 16px; text-decoration: none; letter-spacing: 0.3px;
  }

  .site-footer {
    position: absolute; left: 0; right: 0; bottom: 0; height: 62px;
    background: var(--footer-bg);
    display: flex; align-items: center; justify-content: center;
    font-size: 14px;
  }
</style>
</head>
<body>
  <div class="page">
    <div class="hero-backdrop" role="img" aria-label="Upward view of glass office towers against a blue sky with warm sunset light"></div>

    <header class="site-header">
      <div class="brand">TR VENTURA</div>
      <nav class="main-nav">
        <a href="#" class="is-active">HOME</a>
        <a href="#">ABOUT</a>
        <a href="#">WHY</a>
        <a href="#">PROJECTS</a>
      </nav>
    </header>

    <main class="hero">
      <h1 class="hero-title">TR VENTURA</h1>
      <p class="hero-lead">We are an Holding Company that owns other companie’s shares in different fields</p>
      <a href="#" class="cta">GET MORE INFO</a>
    </main>

    <footer class="site-footer">Copyright © 2017 TR Ventura. All rights reserved.</footer>
  </div>
</body>
</html>
```